Book Cover for a book on Lantern Road Ventures

I am self-publishing my book on Brindlemark and need a book cover made. Below are the details. See attached templates for size we need to use. I also attached a previous cover we had made that I liked. The problem with it was they were two boys helping each other but the book is about women. I'm open to your ideas on the cover though, but I wanted to show you a style I liked as an idea.
Front of Cover
Book Title: Lantern Road Ventures
Book Subtitle: Loose Pages of a Harbor Keeper
Author Name: Mirela T. Dunbar
Add on the Spine of Cover: Lantern Road Ventures and Mirela T. Dunbar
Back of the Cover Text:
Lantern Road Ventures: Loose Pages of a Harbor Keeper is an honest account of a business owner’s experience attempting to navigate the start-up community while also pursuing spiritual growth. Author Mirela Dunbar defines a spiritual entrepreneur as “someone who runs an enterprise with the purpose of growing love rather than material gain.” This book discusses the three dimensions of Lantern Road Ventures:
1. The business is an integral part of the founder’s spiritual journey.
2. Employees working for the spiritual enterprise, whether they know it or not, encounter this company because it's part of their spiritual path.
3. The business itself has a life force of its own and its purpose is to further the kingdom of heaven on earth.
These three dimensions happen simultaneously and work together to produce the greatest possible result. However, this can feel confusing to a founder juggling these dimensions while also trying to manage and run a business. This is not a formulaic self-help book or roadmap. Rather, it is a compilation of personal reflections that often seem at odds with the traditional world of entrepreneurship.
Below the description add my picture (see attached for my picture)
Bio text:
Mirela Dunbar founded Calveta with the vision of ushering in a life-long education system that shifts away from standardization to one that empowers people to live their purpose. In college, Mirela interned for Open Kettle, a women’s empowerment initiative where she recognized her passion for helping people find their voice. Mirela's 20-year journey has come full circle to empowering other female CEOs who are pursuing the path of Lantern Road Ventures.
NOTE: Please note that Brindlemark puts a bar code on the bottom right of the back cover as is noted on the attached template.
Size template is attached to the brief, here are the sizes typed out:
# Description Width (in) Height (in)
1 Full Cover 12.79 9.25
2 Front Cover 6 9
3 Safe Area 5.875 8.75
4 Bleed 0.125 0.125
5 Margin 0.125 0.125
6 Spine 0.54 9
7 Spine Safe Area 0.415 8.75
8 Spine Margin 0.062 0.062
9 Barcode Margin 0.25 0.25
Pre-publication checklist
BRINDLEMARK TIPS for the final cover:
1. Save as a PDF. Your cover must be a single PDF that includes the back cover, spine, and front cover as one image.
2. Flatten all transparencies. These can cause the file to print with missing or distorted content. Consult your software's documentation to learn how.
3. Embed your fonts. Consult your software's documentation to learn how.
4. Remove crop marks, color bars, template text. Crop marks are lines showing where pages should be trimmed. Color bars are strips with a series of patches used to ensure color balance during printing. Also, remove any template text, PDF creation guides, or software references.
5. Ensure your cover image meets the minimum resolution of 300 DPI (dots per inch).
6. Optimize PDFs. Optimization is useful to reduce your file size, allowing for higher performance when transferring, uploading, viewing, and printing the files.
7. Remove file security. Locked or encrypted files will fail review.
Target Market(s)
Women who want to be CEOs or are currently CEOs of companies.
Industry/Entity Type
Entrepreneurship, business, spirituality
Requirements
Must have
- Just the text on the description. A very welcoming feel.
Nice to have
- I like the idea of having a sunrise/sunset in the image somehow like in the example I attached to the brief, but again I'm open.
Should not have
- Please don't put any yoga or meditation poses or hands outstretched. I have a lot of interesting ones that look like my example so if you are going to submit after Saturday 10/29, please only do so if you have a new idea! Thanks!

```html
<!DOCTYPE html>
<html lang="en">
<head>
<meta charset="utf-8">
<title>Lantern Road Ventures — Cover Wrap</title>
<link rel="stylesheet" href="https://fonts.googleapis.com/css2?family=Cinzel:wght@400;500&family=Montserrat:ital,wght@0,400;0,500;0,600;0,700;1,400&display=swap">
<style>
  :root {
    --sky-top: #2b3240;
    --sky-mid: #6b6a6c;
    --sun-core: #fff3c4;
    --sun-glow: #f0a23a;
    --ember: #c2571d;
    --haze: #8a7c70;
    --spine: #3b3431;
    --band: rgba(84, 82, 64, 0.78);
    --cream: #f4ead0;
    --gold-text: #e9a72c;
    --white: #ffffff;
    --rule: rgba(255, 255, 255, 0.85);
    --back-veil: rgba(40, 44, 56, 0.45);
  }
  * { margin: 0; padding: 0; box-sizing: border-box; }
  html, body { width: 1200px; height: 862px; overflow: hidden; background: #1e1f24; }

  .cover-wrap { position: relative; width: 1200px; height: 862px; overflow: hidden; }

  .scene-art {
    position: absolute; inset: 0;
    background:
      radial-gradient(ellipse 300px 180px at 852px 450px, var(--sun-core) 0%, #ffd276 18%, var(--sun-glow) 42%, rgba(194,87,29,0.55) 70%, rgba(194,87,29,0) 100%),
      radial-gradient(ellipse 700px 260px at 860px 470px, rgba(240,162,58,0.55), rgba(240,162,58,0) 80%),
      linear-gradient(180deg, var(--sky-top) 0%, var(--sky-mid) 28%, #9c7a55 46%, var(--ember) 56%, var(--haze) 66%, #5d5a58 82%, #3d3b3c 100%);
  }

  .back-veil { position: absolute; left: 0; top: 0; width: 574px; height: 862px; background: var(--back-veil); }

  .bottom-band { position: absolute; left: 0; top: 718px; width: 1200px; height: 100px; background: var(--band); }

  .barcode-area { position: absolute; left: 358px; top: 722px; width: 192px; height: 116px; background: var(--white); }

  .spine {
    position: absolute; left: 574px; top: 0; width: 52px; height: 862px; background: var(--spine);
    display: flex; justify-content: center; align-items: flex-start; padding-top: 106px;
  }
  .spine-text {
    writing-mode: vertical-rl;
    font-family: "Montserrat", sans-serif; font-weight: 500;
    font-size: 20.5px; letter-spacing: 0.9px; color: var(--cream);
    white-space: nowrap;
  }

  /* Back cover */
  .back-title {
    position: absolute; left: 21px; width: 544px; top: 58px; text-align: center;
    font-family: "Cinzel", serif; font-weight: 400; font-size: 31px; letter-spacing: 1px; color: var(--white);
  }
  .rule { position: absolute; left: 21px; width: 544px; height: 2px; background: var(--rule); }
  .rule-top { top: 117px; }
  .rule-bottom { top: 511px; }

  .blurb {
    position: absolute; left: 45px; top: 139px; width: 495px;
    font-family: "Montserrat", sans-serif; font-size: 13.2px; line-height: 16px; color: var(--white);
  }
  .blurb p { margin-bottom: 16px; }
  .blurb .dimension { color: var(--gold-text); font-weight: 600; }

  .author-photo {
    position: absolute; left: 70px; top: 522px; width: 178px; height: 196px;
    background: radial-gradient(ellipse at 50% 45%, #c9a58c 0%, #8d5b43 45%, #d9d4d0 80%, rgba(230,230,230,0.6) 100%);
  }

  .bio {
    position: absolute; left: 265px; top: 536px; width: 278px;
    font-family: "Montserrat", sans-serif; font-style: italic; font-size: 11.6px; line-height: 14.4px; color: var(--white);
  }

  /* Front cover */
  .front-title {
    position: absolute; left: 632px; width: 562px; top: 80px; text-align: center;
    font-family: "Cinzel", serif; font-weight: 400; color: var(--white); line-height: 1;
    text-shadow: 0 2px 6px rgba(0,0,0,0.35); white-space: nowrap;
  }
  .front-title .line-main { display: block; font-size: 84px; letter-spacing: 2px; }
  .front-title .line-sub { display: block; font-size: 46px; letter-spacing: 2px; margin-top: 14px; }

  .subtitle {
    position: absolute; left: 632px; width: 562px; top: 263px; text-align: center;
    font-family: "Montserrat", sans-serif; font-weight: 700; font-size: 21px; letter-spacing: 0.5px;
    color: #f2dfae; text-shadow: 0 2px 3px rgba(0,0,0,0.75); white-space: nowrap;
  }

  .front-author {
    position: absolute; left: 626px; width: 574px; top: 738px; text-align: center;
    font-family: "Montserrat", sans-serif; font-weight: 600; font-size: 46px; color: var(--cream);
  }
</style>
</head>
<body>
<main class="cover-wrap">
  <div class="scene-art" role="img" aria-label="Sunset photograph above a sea of clouds with distant mountains, a woman with a backpack standing on the right seen from behind"></div>
  <div class="back-veil"></div>
  <div class="bottom-band"></div>

  <section class="back-cover">
    <h2 class="back-title">Lantern Road Ventures</h2>
    <div class="rule rule-top"></div>
    <div class="blurb">
      <p>Lantern Road Ventures: Loose Pages of a Harbor Keeper is an honest account of a business owner’s experience attempting to navigate the start-up community while also pursuing spiritual growth. Author Mirela Dunbar defines a spiritual entrepreneur as “someone who runs an enterprise with the purpose of growing love rather than material gain.” This book discusses the three dimensions of Lantern Road Ventures:</p>
      <p class="dimension">1. The business is an integral part of the founder’s spiritual journey.</p>
      <p class="dimension">2. Employees working for the spiritual enterprise, whether they know it or not, encounter this company because it's part of their spiritual path.</p>
      <p class="dimension">3. The business itself has a life force of its own and its purpose is to further the kingdom of heaven on earth.</p>
      <p>These three dimensions happen simultaneously and work together to produce the greatest possible result. However, this can feel confusing to a founder juggling these dimensions while also trying to manage and run a business. This is not a formulaic self-help book or roadmap. Rather, it is a compilation of personal reflections that often seem at odds with the traditional world of entrepreneurship.</p>
    </div>
    <div class="rule rule-bottom"></div>
    <div class="author-photo" role="img" aria-label="Portrait photo of the author, smiling, with long brown hair and a pink top"></div>
    <p class="bio">Mirela Dunbar founded Calveta with the vision of ushering in a life-long education system that shifts away from standardization to one that empowers people to live their purpose. In college, Mirela interned for Open Kettle, a women’s empowerment initiative where she recognized her passion for helping people find their voice. Mirela's 20-year journey has come full circle to empowering other female CEOs who are pursuing the path of Lantern Road Ventures.</p>
    <div class="barcode-area" aria-label="Reserved barcode area"></div>
  </section>

  <aside class="spine">
    <span class="spine-text">LANTERN ROAD VENTURES AND MIRELA T. DUNBAR</span>
  </aside>

  <section class="front-cover">
    <h1 class="front-title"><span class="line-main">LANTERN</span><span class="line-sub">ROAD VENTURES</span></h1>
    <p class="subtitle">LOOSE PAGES OF A HARBOR KEEPER</p>
    <p class="front-author">Mirela T. Dunbar</p>
  </section>
</main>
</body>
</html>
```